A flyer for future customers to get acquainted with our company

The flyer/card is intended for intermediaries. The purpose of this flyer is to introduce businesses to Dovrel.

It should convey: real estate and financing, with actual images. Various keywords describing what we do: project financing, temporary real estate financing, real estate financing, investment properties, transformations. We distinguish ourselves by being fast, flexible, and personal.

Please ensure the front has an attractive and inviting appearance, and leave space on the back for additional text.

Color codes: #E85B35 en #091E33

```html
<!DOCTYPE html>
<html lang="en">
<head>
<meta charset="utf-8">
<title>Dovrel – Real Estate and Financing Postcard</title>
<link rel="stylesheet" href="https://fonts.googleapis.com/css2?family=Merriweather:wght@700;900&family=Poppins:wght@400;500&display=swap">
<style>
:root{
  --orange:#E85B35;
  --navy:#091E33;
  --white:#ffffff;
  --ink:#14202e;
  --page:#e4e2df;
  --rule:#b9bec5;
  --serif:"Merriweather", Georgia, serif;
  --sans:"Poppins", Arial, sans-serif;
}
*{box-sizing:border-box;margin:0;padding:0}
html,body{width:1129px;height:1200px;overflow:hidden}
body{background:var(--page);font-family:var(--sans);position:relative}
.card{position:absolute;left:124px;width:880px;height:564px;overflow:hidden;background:var(--white);box-shadow:0 8px 18px rgba(0,0,0,.22)}
.card--front{top:24px}
.card--back{top:612px}
.card__art{position:absolute;inset:0}
.layer{position:absolute}

.brand{font-family:var(--serif);font-weight:700;font-size:40px;line-height:1;letter-spacing:-.5px;color:var(--white)}
.brand--dark{color:var(--navy);font-size:36px}

.headline{font-family:var(--serif);font-weight:900;font-size:33px;line-height:1.08}
.headline__top{color:var(--orange);display:block}
.headline__bottom{color:var(--white);display:block}

.intro{color:var(--white);font-size:14px;font-weight:500}

.values{display:flex}
.value{width:93px;display:flex;flex-direction:column;align-items:center;gap:9px;border-right:1.5px solid rgba(255,255,255,.7)}
.value:last-child{border-right:none}
.value__icon{width:50px;height:50px;border-radius:50%;background:var(--white);border:3px solid var(--orange);display:flex;align-items:center;justify-content:center}
.value__label{color:var(--orange);font-size:13.5px;font-weight:500}

.services__title{font-family:var(--serif);font-weight:900;font-size:17px;color:var(--navy);margin-bottom:7px}
.services__list{list-style:none}
.services__list li{color:var(--white);font-size:14px;line-height:26.5px;display:flex;align-items:center;gap:12px}
.tick{width:14px;height:14px;flex:none}

.contact{display:flex;align-items:center;gap:14px;color:var(--ink)}
.contact__item{display:flex;align-items:center;gap:8px;font-size:14px;font-weight:500}
.contact__item--phone{font-size:20px}
.contact__icon{width:16px;height:16px;flex:none}
.accent{color:var(--orange)}

.story__title{font-family:var(--serif);font-weight:900;font-size:17px;color:var(--navy);margin-bottom:8px}
.story__text{color:var(--white);font-size:12px;line-height:15.6px;text-align:justify}

.sender{display:flex;flex-direction:column;gap:4px}
.sender__line{display:flex;align-items:center;gap:7px;font-size:14px;font-weight:500;color:var(--ink)}
.sender__line--small{font-size:11.5px}
.stamp-box{position:absolute;left:736px;top:22px;width:108px;height:108px;border:1.5px solid var(--rule)}
.address-line{position:absolute;left:598px;width:246px;height:1.5px;background:var(--rule)}
</style>
</head>
<body>

<section class="card card--front" aria-label="Postcard front">
  <svg class="card__art" viewBox="0 0 880 564" width="880" height="564">
    <defs>
      <linearGradient id="teamPhotoTone" x1="0" y1="0" x2="1" y2="1">
        <stop offset="0" stop-color="#4a4440"/>
        <stop offset=".45" stop-color="#8a7a72"/>
        <stop offset=".75" stop-color="#b8b0aa"/>
        <stop offset="1" stop-color="#6f7078"/>
      </linearGradient>
      <radialGradient id="modelPhotoTone" cx=".5" cy=".45" r=".6">
        <stop offset="0" stop-color="#c9b4a4"/>
        <stop offset=".6" stop-color="#6e6258"/>
        <stop offset="1" stop-color="#2b2a2c"/>
      </radialGradient>
    </defs>
    <rect width="880" height="564" fill="url(#teamPhotoTone)" role="img" aria-label="Photo: real estate advisors working together over a white architectural model of houses"/>
    <path d="M0,0 H322 C310,110 318,220 356,300 H0 Z" fill="var(--navy)"/>
    <path d="M322,0 C310,110 318,220 356,300" fill="none" stroke="var(--orange)" stroke-width="4"/>
    <path d="M0,297 H356 C420,330 470,400 515,459 C545,495 575,530 600,564 H0 Z" fill="var(--orange)"/>
    <path d="M515,459 C550,495 585,530 620,564" fill="none" stroke="var(--navy)" stroke-width="5"/>
    <path d="M0,493 H520 C555,500 585,528 605,564 H0 Z" fill="var(--white)"/>
    <circle cx="427" cy="323" r="128" fill="url(#modelPhotoTone)" stroke="var(--navy)" stroke-width="3" role="img" aria-label="Photo: woman studying a model of apartment buildings"/>
  </svg>

  <div class="layer brand" style="left:34px;top:30px">Dovrel</div>

  <h1 class="layer headline" style="left:34px;top:89px">
    <span class="headline__top">Real Estate</span>
    <span class="headline__bottom">And Financing</span>
  </h1>

  <p class="layer intro" style="left:34px;top:173px">We Distinguish Ourselves By:</p>

  <div class="layer values" style="left:12px;top:205px">
    <div class="value">
      <span class="value__icon">
        <svg width="26" height="26" viewBox="0 0 26 26" fill="none" stroke="var(--navy)" stroke-width="1.8" stroke-linecap="round"><path d="M5 9 H19 L15 5 M21 17 H7 L11 21"/></svg>
      </span>
      <span class="value__label">Flexible</span>
    </div>
    <div class="value">
      <span class="value__icon">
        <svg width="26" height="26" viewBox="0 0 26 26" fill="none" stroke-linecap="round" stroke-width="1.8"><circle cx="15" cy="13" r="8" stroke="var(--navy)"/><path d="M15 8 V13 L18 15" stroke="var(--orange)"/><path d="M2 10 H6 M3 14 H6 M2 18 H7" stroke="var(--orange)"/></svg>
      </span>
      <span class="value__label">Being Fast</span>
    </div>
    <div class="value">
      <span class="value__icon">
        <svg width="26" height="26" viewBox="0 0 26 26" fill="none" stroke="var(--navy)" stroke-width="1.8" stroke-linecap="round"><circle cx="13" cy="10" r="4"/><path d="M6 21 C7 16 19 16 20 21"/></svg>
      </span>
      <span class="value__label">Personal</span>
    </div>
  </div>

  <div class="layer services" style="left:34px;top:322px">
    <h2 class="services__title">What We Do:</h2>
    <ul class="services__list">
      <li><svg class="tick" viewBox="0 0 14 14" fill="none" stroke="var(--white)" stroke-width="1.5" stroke-linecap="round"><path d="M12 6.5 A5.5 5.5 0 1 1 9.5 2.3"/><path d="M4.5 7 L7 9.3 L12.5 3"/></svg>Project Financing</li>
      <li><svg class="tick" viewBox="0 0 14 14" fill="none" stroke="var(--white)" stroke-width="1.5" stroke-linecap="round"><path d="M12 6.5 A5.5 5.5 0 1 1 9.5 2.3"/><path d="M4.5 7 L7 9.3 L12.5 3"/></svg>Real Estate Financing</li>
      <li><svg class="tick" viewBox="0 0 14 14" fill="none" stroke="var(--white)" stroke-width="1.5" stroke-linecap="round"><path d="M12 6.5 A5.5 5.5 0 1 1 9.5 2.3"/><path d="M4.5 7 L7 9.3 L12.5 3"/></svg>Investment Properties</li>
      <li><svg class="tick" viewBox="0 0 14 14" fill="none" stroke="var(--white)" stroke-width="1.5" stroke-linecap="round"><path d="M12 6.5 A5.5 5.5 0 1 1 9.5 2.3"/><path d="M4.5 7 L7 9.3 L12.5 3"/></svg>Transformations</li>
      <li><svg class="tick" viewBox="0 0 14 14" fill="none" stroke="var(--white)" stroke-width="1.5" stroke-linecap="round"><path d="M12 6.5 A5.5 5.5 0 1 1 9.5 2.3"/><path d="M4.5 7 L7 9.3 L12.5 3"/></svg>Temporary Real Estate Financing</li>
    </ul>
  </div>

  <div class="layer contact" style="left:34px;top:518px">
    <span class="contact__item contact__item--phone">
      <svg class="contact__icon" viewBox="0 0 16 16" fill="none" stroke="var(--orange)" stroke-width="1.3"><circle cx="8" cy="8" r="7"/><path d="M5.5 4.5 L7 6 L6.2 7 C6.8 8.3 7.7 9.2 9 9.8 L10 9 L11.5 10.5 L10.5 11.5 C7.5 11 5 8.5 4.5 5.5 Z"/></svg>
      555-214-7730
    </span>
    <span class="contact__item">
      <svg class="contact__icon" viewBox="0 0 16 16" fill="none" stroke="var(--orange)" stroke-width="1.3"><circle cx="8" cy="8" r="7"/><rect x="4.5" y="5.5" width="7" height="5"/><path d="M4.5 5.5 L8 8.3 L11.5 5.5"/></svg>
      <span>www.<span class="accent">dovrel</span>.com</span>
    </span>
    <span class="contact__item">
      <svg class="contact__icon" viewBox="0 0 16 16" fill="none" stroke="var(--orange)" stroke-width="1.3"><circle cx="8" cy="8" r="7"/><circle cx="8" cy="8" r="3.5"/><path d="M4.5 8 H11.5 M8 4.5 V11.5"/></svg>
      <span><span class="accent">hello</span>@dovrel-mail.com</span>
    </span>
  </div>
</section>

<section class="card card--back" aria-label="Postcard back">
  <svg class="card__art" viewBox="0 0 880 564" width="880" height="564">
    <defs>
      <linearGradient id="skylineTone" x1="0" y1="0" x2="1" y2="0">
        <stop offset="0" stop-color="var(--navy)"/>
        <stop offset=".55" stop-color="#14406e"/>
        <stop offset="1" stop-color="#1d5a93"/>
      </linearGradient>
      <linearGradient id="cashTone" x1="0" y1="0" x2="1" y2="1">
        <stop offset="0" stop-color="#c98a6c"/><stop offset="1" stop-color="#e9dccd"/>
      </linearGradient>
      <linearGradient id="chartTone" x1="0" y1="0" x2="0" y2="1">
        <stop offset="0" stop-color="#8fbfe3"/><stop offset="1" stop-color="#3b6f9c"/>
      </linearGradient>
      <linearGradient id="pylonTone" x1="0" y1="0" x2="0" y2="1">
        <stop offset="0" stop-color="#9fb6c8"/><stop offset="1" stop-color="#e7c79a"/>
      </linearGradient>
    </defs>
    <rect width="880" height="564" fill="var(--navy)"/>
    <rect x="230" y="0" width="260" height="300" fill="url(#skylineTone)" role="img" aria-label="Photo: blue-toned city skyline of office towers"/>
    <path d="M0,222 C160,208 330,205 490,222 L700,564 H0 Z" fill="var(--orange)"/>
    <path d="M458,0 C462,250 552,460 692,564 H880 V0 Z" fill="var(--navy)"/>
    <path d="M466,0 C470,250 560,460 700,564 H880 V0 Z" fill="var(--white)"/>
    <path d="M0,505 H560 C600,515 630,540 650,564 H0 Z" fill="var(--white)"/>
    <circle cx="85" cy="244" r="53" fill="url(#cashTone)" stroke="var(--white)" stroke-width="3" role="img" aria-label="Photo: hands exchanging house keys and money"/>
    <circle cx="219" cy="244" r="53" fill="url(#chartTone)" stroke="var(--white)" stroke-width="3" role="img" aria-label="Photo: city buildings with a rising growth arrow"/>
    <circle cx="355" cy="244" r="53" fill="url(#pylonTone)" stroke="var(--white)" stroke-width="3" role="img" aria-label="Photo: power transmission towers at sunset"/>
  </svg>

  <div class="layer brand" style="left:32px;top:30px">Dovrel</div>

  <h2 class="layer headline" style="left:32px;top:89px">
    <span class="headline__top">Real Estate</span>
    <span class="headline__bottom">And Financing</span>
  </h2>

  <div class="layer story" style="left:34px;top:320px;width:420px">
    <h3 class="story__title">Where does it come from?</h3>
    <p class="story__text">Contrary to popular belief, Lorem Ipsum is not simply random text. It has roots in a piece of classical Latin literature from 45 BC, making it over 2000 years old. Martin Hale, a Latin professor at Ashford College in Vermont, looked up one of the more obscure Latin words, consectetur, from a Lorem Ipsum passage, and going through the cites of the word in classical literature, discovered the undoubtable source.</p>
  </div>

  <div class="layer sender" style="left:586px;top:30px">
    <div class="brand brand--dark">Dovrel</div>
    <span class="sender__line">
      <svg class="contact__icon" viewBox="0 0 16 16" fill="none" stroke="var(--orange)" stroke-width="1.3"><circle cx="8" cy="8" r="7"/><path d="M5.5 4.5 L7 6 L6.2 7 C6.8 8.3 7.7 9.2 9 9.8 L10 9 L11.5 10.5 L10.5 11.5 C7.5 11 5 8.5 4.5 5.5 Z"/></svg>
      555-214-7730
    </span>
    <span class="sender__line sender__line--small">
      <svg class="contact__icon" viewBox="0 0 16 16" fill="none" stroke="var(--orange)" stroke-width="1.3"><circle cx="8" cy="8" r="7"/><rect x="4.5" y="5.5" width="7" height="5"/><path d="M4.5 5.5 L8 8.3 L11.5 5.5"/></svg>
      <span>www.<span class="accent">dovrel</span>.com</span>
    </span>
  </div>

  <div class="stamp-box" aria-label="Stamp area"></div>
  <div class="address-line" style="top:236px"></div>
  <div class="address-line" style="top:308px"></div>
  <div class="address-line" style="top:381px"></div>

  <div class="layer contact" style="left:34px;top:518px">
    <span class="contact__item contact__item--phone">
      <svg class="contact__icon" viewBox="0 0 16 16" fill="none" stroke="var(--orange)" stroke-width="1.3"><circle cx="8" cy="8" r="7"/><path d="M5.5 4.5 L7 6 L6.2 7 C6.8 8.3 7.7 9.2 9 9.8 L10 9 L11.5 10.5 L10.5 11.5 C7.5 11 5 8.5 4.5 5.5 Z"/></svg>
      555-214-7730
    </span>
    <span class="contact__item">
      <svg class="contact__icon" viewBox="0 0 16 16" fill="none" stroke="var(--orange)" stroke-width="1.3"><circle cx="8" cy="8" r="7"/><rect x="4.5" y="5.5" width="7" height="5"/><path d="M4.5 5.5 L8 8.3 L11.5 5.5"/></svg>
      <span>www.<span class="accent">dovrel</span>.com</span>
    </span>
    <span class="contact__item">
      <svg class="contact__icon" viewBox="0 0 16 16" fill="none" stroke="var(--orange)" stroke-width="1.3"><circle cx="8" cy="8" r="7"/><circle cx="8" cy="8" r="3.5"/><path d="M4.5 8 H11.5 M8 4.5 V11.5"/></svg>
      <span><span class="accent">hello</span>@dovrel-mail.com</span>
    </span>
  </div>
</section>

</body>
</html>
```